Creative, fresh business card design for Orrin Linings

We need a fresh, creative business card design for Orrin Linings. We are the manufacturer of Orrin Linings in Australia. Wall panels are 2400 x 1200mm panels made from MDF and feature 3D patterns on the face of the panel. The colours to be used are green, silver/grey and white RGB
Red 187
Green 207
Blue 65.

An idea is to possibly use a watermark of one of our designs as a background (like on the "Ferns" design on the left hand side of page 2 of our brochure).

Target Market(s)

Interior designers, architects, builders and home renovators

Industry/Entity Type

Business

Contact Information for Business Card

Details to go on the card are:
Our logo (attached),
Slogan: "Decorative panels for interiors and exteriors",
Contact name,
Position,
Mobile phone number,
Business address,
Business phone,
Business fax,
Website and
Email address.

I have attached a few images of our panels and our brochure for reference.

The colours of the business card should feature our logo colours which are: RGB
Red 187
Green 207
Blue 65

Requirements
Must have
• Very modern fonts and design. Some of the designs shown especially the "Weave" design which is a popular design.
Nice to have
• Creative but simple design. Very contemporary.
Should not have
• Anything ornate or old fashioned.

```html
<!DOCTYPE html>
<html lang="en">
<head>
<meta charset="utf-8">
<title>Orrin Linings – Business Card</title>
<link rel="stylesheet" href="https://fonts.googleapis.com/css2?family=Cormorant+Garamond:wght@500&family=PT+Sans+Narrow:wght@400;700&family=Open+Sans:wght@400;600&display=swap">
<style>
  :root {
    --brand-green: rgb(187, 207, 65);
    --brand-green-deep: #a9bf2f;
    --silver: #8e8f91;
    --ink: #2b2b2b;
    --white: #ffffff;
    --backdrop: #e6e6e6;
  }
  * { box-sizing: border-box; margin: 0; padding: 0; }
  html, body { width: 1200px; height: 1200px; overflow: hidden; }
  body {
    background: var(--backdrop);
    font-family: "PT Sans Narrow", "Arial Narrow", sans-serif;
    color: var(--ink);
  }
  .sheet {
    width: 1200px; height: 1200px;
    display: flex; flex-direction: column; align-items: center; justify-content: center;
    gap: 60px;
  }
  .card {
    position: relative;
    width: 860px; height: 520px;
    box-shadow: 0 6px 22px rgba(0,0,0,.14);
    overflow: hidden;
  }

  /* ---------- Front ---------- */
  .card--front { background: var(--white); }
  .card__texture {
    position: absolute; inset: 0;
    background: radial-gradient(ellipse at 35% 25%, #efeff0 0%, rgba(255,255,255,0) 60%);
  }
  .contact {
    position: absolute; left: 64px; top: 70px; width: 440px;
  }
  .contact__name {
    font-family: "Cormorant Garamond", Georgia, serif;
    font-weight: 500;
    font-size: 44px; letter-spacing: 1px;
    color: var(--brand-green);
    text-transform: uppercase;
    line-height: 1;
  }
  .contact__role, .contact__line {
    font-size: 22px; display: flex; align-items: center; gap: 8px;
  }
  .contact__role { margin-top: 10px; }
  .contact__line { margin-top: 8px; }
  .icon { width: 16px; height: 16px; fill: var(--brand-green); flex: none; }
  .contact__rule {
    height: 2px; background: var(--brand-green);
    margin: 22px 0 16px;
  }
  .contact__columns { display: flex; }
  .contact__col { padding-right: 20px; }
  .contact__col + .contact__col {
    border-left: 1px solid var(--brand-green);
    padding-left: 20px;
  }
  .contact__col .contact__line:first-child { margin-top: 0; }

  .brand {
    position: absolute; right: 60px; bottom: 90px; width: 330px;
  }
  .brand__mark { display: flex; align-items: center; gap: 12px; }
  .brand__square { width: 34px; height: 34px; background: var(--brand-green); flex: none; }
  .brand__name {
    font-family: "PT Sans Narrow", "Arial Narrow", sans-serif;
    font-weight: 700; font-size: 46px; line-height: 1;
    color: var(--brand-green);
  }
  .brand__tagline {
    margin-top: 14px;
    font-family: "Open Sans", Arial, sans-serif;
    font-size: 15px; letter-spacing: 4px; line-height: 1.5;
    color: var(--silver);
  }

  /* ---------- Back ---------- */
  .card--back {
    background: linear-gradient(120deg, var(--brand-green-deep) 0%, var(--brand-green) 45%, var(--brand-green-deep) 100%);
    display: flex; align-items: center; justify-content: center;
  }
  .card--back .card__texture {
    background: radial-gradient(ellipse at 60% 40%, rgba(255,255,255,.14) 0%, rgba(255,255,255,0) 65%);
  }
  .slogan {
    position: relative;
    font-family: "Open Sans", Arial, sans-serif;
    font-weight: 600; font-size: 46px; line-height: 1.25;
    color: var(--white); text-align: center; letter-spacing: 1px;
    text-shadow: 0 2px 3px rgba(0,0,0,.22);
  }
</style>
</head>
<body>
<main class="sheet">

  <section class="card card--front" aria-label="Business card front">
    <div class="card__texture" role="img" aria-label="Faint watermark of a panel pattern"></div>

    <div class="contact">
      <h1 class="contact__name">Calla Brennick</h1>
      <p class="contact__role">Director /
        <svg class="icon" viewBox="0 0 16 16" aria-hidden="true"><rect x="4" y="1" width="8" height="14" rx="1.5"/></svg>
        0400-555-218</p>
      <p class="contact__line">
        <svg class="icon" viewBox="0 0 16 16" aria-hidden="true"><path d="M8 1 1 8h2v7h4v-4h2v4h4V8h2z"/></svg>
        14 Tallow Road, Kelso Vale NSW 2170</p>
      <div class="contact__rule"></div>
      <div class="contact__columns">
        <div class="contact__col">
          <p class="contact__line">
            <svg class="icon" viewBox="0 0 16 16" aria-hidden="true"><path d="M3 2h3l1 3-2 1a8 8 0 0 0 5 5l1-2 3 1v3a1 1 0 0 1-1 1A12 12 0 0 1 2 3a1 1 0 0 1 1-1z"/></svg>
            02 5550 1840</p>
          <p class="contact__line">
            <svg class="icon" viewBox="0 0 16 16" aria-hidden="true"><path d="M4 1h7v4H4zM1 6h14v7h-3v2H4v-2H1zm4 5v3h6v-3z"/></svg>
            02 5550 1847</p>
        </div>
        <div class="contact__col">
          <p class="contact__line">
            <svg class="icon" viewBox="0 0 16 16" aria-hidden="true"><path d="M8 1a7 7 0 1 0 0 14A7 7 0 0 0 8 1zm0 2c.8 1 1.3 2.4 1.5 4h-3C6.7 5.4 7.2 4 8 3zM3.1 9h2.4c.1 1.4.5 2.7 1 3.7A5 5 0 0 1 3.1 9zm0-2a5 5 0 0 1 3.4-3.7c-.5 1-.9 2.3-1 3.7zm4.9 6c-.8-1-1.3-2.4-1.5-4h3c-.2 1.6-.7 3-1.5 4zm1.5-.3c.5-1 .9-2.3 1-3.7h2.4a5 5 0 0 1-3.4 3.7zM10.5 7c-.1-1.4-.5-2.7-1-3.7A5 5 0 0 1 12.9 7z"/></svg>
            www.orrinlinings.com.au</p>
          <p class="contact__line">
            <svg class="icon" viewBox="0 0 16 16" aria-hidden="true"><path d="M1 3h14v10H1zm1.5 1.5L8 9l5.5-4.5z"/></svg>
            sales@orrinlinings.com.au</p>
        </div>
      </div>
    </div>

    <div class="brand">
      <div class="brand__mark">
        <span class="brand__square" aria-hidden="true"></span>
        <span class="brand__name">Orrin Linings</span>
      </div>
      <p class="brand__tagline">decorative panels for<br>interiors &amp; landscapes</p>
    </div>
  </section>

  <section class="card card--back" aria-label="Business card back">
    <div class="card__texture" role="img" aria-label="Faint watermark of a panel pattern"></div>
    <p class="slogan">Decorative panels<br>for<br>interiors and exteriors</p>
  </section>

</main>
</body>
</html>
```